Re-design of Business card and ESP formatting of Logo
Quonvera
Re-design of Business card and ESP formatting of Logo - Construction
Creative Brief
Professional
Dale Voss
Vice President of Sales
4875 Maplecrest Ave. suite K Charlotte, NC 28391
DVoss@quonverainc.example
www.quonverainc.example
Please see the current business card and Logo. I would like the new logo incorporated into the business card
Cleaning up the past, making way for the future
Pelbrook7 Pelbrook7
The current Logos I would like touched up and done in an esp file so I can use them for printing banners, shirts, signs, etc.

```html
<!DOCTYPE html>
<html lang="en">
<head>
<meta charset="utf-8">
<title>Quonvera Business Card</title>
<link rel="stylesheet" href="https://fonts.googleapis.com/css2?family=Open+Sans:wght@400;600;700&display=swap">
<style>
  :root {
    --backdrop: #5f4c3e;
    --navy: #02034a;
    --green: #00ff00;
    --white: #ffffff;
    --card-shadow: rgba(0, 0, 0, 0.45);
  }
  html, body {
    margin: 0;
    padding: 0;
    width: 1200px;
    height: 987px;
    overflow: hidden;
    background: var(--backdrop);
    font-family: "Open Sans", Arial, sans-serif;
  }
  .canvas {
    position: relative;
    width: 1200px;
    height: 987px;
  }
  .card {
    position: absolute;
    width: 615px;
    height: 351px;
    box-shadow: 0 4px 14px var(--card-shadow);
    overflow: hidden;
  }
  .card--front { left: 293px; top: 130px; background: var(--white); }
  .card--back { left: 292px; top: 506px; background: var(--green); }

  .front-panel {
    position: absolute;
    inset: 0;
    width: 615px;
    height: 351px;
  }
  .front-brand {
    position: absolute;
    left: 20px;
    top: 150px;
    width: 270px;
    text-align: center;
    font-weight: 700;
    font-size: 36px;
    letter-spacing: 1px;
    color: var(--navy);
  }
  .contact {
    position: absolute;
    right: 21px;
    top: 50px;
    text-align: right;
    color: var(--white);
    font-size: 14.5px;
    line-height: 19.5px;
  }
  .contact__name {
    margin: 0;
    color: var(--green);
    font-weight: 600;
    font-size: 23px;
    line-height: 28px;
    letter-spacing: 0.5px;
  }
  .contact__title { margin: 0 0 17px; font-size: 15px; }
  .contact__address { margin: 0 0 16px; }
  .contact__lines { margin: 0; }
  .contact__label { color: var(--green); font-weight: 700; }
  .services {
    position: absolute;
    right: 26px;
    top: 291px;
    margin: 0;
    color: var(--green);
    font-weight: 600;
    font-size: 17px;
  }
  .back-brand {
    position: absolute;
    left: 0;
    right: 0;
    top: 140px;
    text-align: center;
    font-weight: 700;
    font-size: 44px;
    letter-spacing: 1px;
    color: var(--navy);
  }
  .back-web {
    position: absolute;
    left: 0;
    right: 0;
    top: 294px;
    margin: 0;
    text-align: center;
    color: var(--navy);
    font-size: 14px;
    letter-spacing: 4.5px;
  }
</style>
</head>
<body>
<main class="canvas">
  <section class="card card--front">
    <svg class="front-panel" viewBox="0 0 615 351" aria-hidden="true">
      <polygon points="392,0 615,0 615,351 158,351" fill="var(--navy)"/>
      <polygon points="390,0 398,0 164,351 156,351" fill="var(--green)"/>
    </svg>
    <div class="front-brand">QUONVERA</div>
    <div class="contact">
      <p class="contact__name">DALE VOSS</p>
      <p class="contact__title">Vice President of Sales</p>
      <p class="contact__address">4875 Maplecrest Ave. suite K<br>Charlotte, NC 28391</p>
      <p class="contact__lines">
        <span class="contact__label">Phone :</span> 704.555.0142<br>
        <span class="contact__label">Cell :</span> 704.555.0187<br>
        <span class="contact__label">Fax :</span> 704.555.0143<br>
        DVoss@quonverainc.example<br>
        www.quonverainc.example
      </p>
    </div>
    <p class="services">Demolition • Remediation • Crane &amp; Rigging</p>
  </section>

  <section class="card card--back">
    <div class="back-brand">QUONVERA</div>
    <p class="back-web">www.quonverainc.example</p>
  </section>
</main>
</body>
</html>
```